lantern pathway for children needs a website designer

We need a website designer for our new extension to our company known as 'lantern pathway' providing shadow support services to children based in Singapore. We are a sister branch of a private clinic 'Brightwell Learning' providing speech language, occupational, and educational therapy to children.

We would like to use our own photos. So the selected design should have a frame with pictures to give us an idea but we will replace them with our own. We will be needing help with inputting information and changing information throughout.

We would like to see designs that are simple, and professional. We have a logo (see attached). The result should convey professionalism in shadow support, fostering independent thinking and moving students towards self-learning.

Target Market(s)

Teachers, psychologists, parents

Industry/Entity Type

Clinic

Requirements
Should not have
• too distracting colours

```html
<!DOCTYPE html>
<html lang="en">
<head>
<meta charset="utf-8">
<title>Lantern Pathway</title>
<link href="https://fonts.googleapis.com/css2?family=Arimo:ital,wght@0,400;0,700;1,400&display=swap" rel="stylesheet">
<style>
:root{
  --red:#8c1414;
  --red-bright:#c0392b;
  --text:#555;
  --muted:#777;
  --band:#7a7a7a;
  --line:#ddd;
  --light:#f2f2f2;
}
*{box-sizing:border-box;margin:0;padding:0}
html,body{width:866px;height:1200px;overflow:hidden;background:#fff}
body{font-family:"Arimo",Arial,sans-serif;color:var(--text);position:relative}
.abs{position:absolute}
.search{left:124px;top:54px;width:164px;height:23px;border:1px solid #bbb;border-radius:3px;box-shadow:inset 0 1px 2px rgba(0,0,0,.12);font-size:8px;color:#888;padding:6px 10px}
.search svg{position:absolute;right:8px;top:5px}
.brand{left:300px;top:36px;width:266px;text-align:center;font-size:30px;font-weight:700;color:var(--red);letter-spacing:-.5px}
.enquiry{left:588px;top:38px;font-size:8px;line-height:14px;color:#666}
.enquiry h3{font-size:11px;font-weight:400;color:var(--red);margin-bottom:4px}
.nav{left:124px;top:97px;width:618px;height:31px;background:var(--red);display:flex}
.nav a{color:#fff;text-decoration:none;font-size:9px;display:flex;align-items:center;justify-content:center;border-right:1px solid #c05050}
.nav a:last-child{border-right:none}
.hero{left:124px;top:136px;width:618px;height:264px;background:linear-gradient(120deg,#d8dde2,#f4f1ee 45%,#e6c6a8 70%,#f2f2f2)}
.arrows{left:700px;top:376px;display:flex;gap:2px}
.arrows span{width:16px;height:16px;background:var(--red-bright);color:#fff;font-size:10px;display:flex;align-items:center;justify-content:center}
.quote-band{left:124px;top:400px;width:618px;height:103px;background:var(--band);color:#fff}
.quote-band .avatar{position:absolute;left:21px;top:13px;width:82px;height:82px;border-radius:50%;background:linear-gradient(#e9e9e9,#bfbfbf);border:3px solid #ddd}
.quote-band .mark{position:absolute;font-size:30px;font-weight:700;font-family:Georgia,serif}
.quote-band p{position:absolute;left:157px;font-size:7.5px;font-style:italic;line-height:15px}
.quote-band .nav-dots{position:absolute;right:18px;top:16px;font-size:9px}
h2.section{font-size:14px;font-weight:400;color:var(--red)}
.about{left:124px;top:524px;width:240px}
.about h2{margin-left:3px}
.about .brand-small{font-size:22px;font-weight:700;color:var(--red);margin:12px 0 18px 4px}
.about p{font-size:7px;line-height:15.5px;margin-bottom:15px}
.btn-grey{display:inline-block;border:1px solid #bbb;border-radius:2px;background:linear-gradient(#f8f8f8,#e4e4e4);font-size:8px;color:#666;padding:9px 20px;margin-top:0}
.support{left:400px;top:524px;width:342px}
.support h2{margin-bottom:12px}
.item{display:flex;gap:13px;margin-bottom:15px}
.item .icon{width:53px;height:53px;border-radius:50%;background:var(--red);flex-shrink:0;display:flex;align-items:center;justify-content:center;margin-top:4px}
.item h4{font-size:10px;font-weight:400;color:var(--red);margin-bottom:4px}
.item p{font-size:6.5px;line-height:13px}
.item .more{color:var(--red);font-size:6.5px;margin-top:2px}
.register{left:124px;top:794px;width:618px;height:57px}
.register .txt{position:absolute;left:21px;top:15px}
.register h3{font-size:12px;font-weight:400;color:var(--red);margin-bottom:7px}
.register p{font-size:7.5px}
.register .req{position:absolute;left:472px;top:14px;width:126px;height:30px;color:#fff;font-size:11px;display:flex;align-items:center;padding-left:28px}
.services-head{left:124px;top:874px;width:618px;text-align:center}
.services-head p{font-size:10px;margin-top:7px}
.svc{top:930px;width:190px}
.svc .ph{height:100px}
.svc h4{font-size:11px;font-weight:400;color:var(--red);margin:19px 0 7px}
.svc p{font-size:7px;line-height:13.6px}
.footer{left:124px;top:1127px;width:618px;height:52px;border-top:3px solid #e8e8e8;background:linear-gradient(#fafafa,#fff)}
.footer .links{position:absolute;left:18px;top:12px;font-size:6.5px;color:#666;word-spacing:2px}
.footer .copy{position:absolute;left:18px;top:30px;font-size:6.5px;color:#666}
.footer .follow{position:absolute;right:18px;top:12px;display:flex;align-items:center;gap:3px;font-size:6.5px}
.footer .follow span.c{width:18px;height:18px;border-radius:50%}
</style>
</head>
<body>
<div class="abs search">Search :
  <svg width="11" height="11" viewBox="0 0 11 11"><circle cx="4.5" cy="4.5" r="3.5" fill="none" stroke="#444" stroke-width="1.4"/><path d="M7 7l3 3" stroke="#444" stroke-width="1.6"/></svg>
</div>
<div class="abs brand">Lantern Pathway</div>
<div class="abs enquiry">
  <h3>Make An Enquiry</h3>
  Phone : +65 6000 1234<br>Email : enquiries@brightwelllearning.example
</div>
<nav class="abs nav">
  <a style="width:92px">Home</a><a style="width:95px">About Us</a><a style="width:94px">Services</a><a style="width:124px">Shadow Support</a><a style="width:111px">For Referrers</a><a style="width:102px">Contact us</a>
</nav>
<div class="abs hero" role="img" aria-label="Photo of two clinicians in white coats working in a bright lab"></div>
<div class="abs arrows"><span>&lsaquo;</span><span>&rsaquo;</span></div>
<div class="abs quote-band">
  <div class="avatar" role="img" aria-label="Portrait of the researcher quoted"></div>
  <span class="mark" style="left:126px;top:12px">&ldquo;</span>
  <span class="mark" style="left:584px;top:44px">&rdquo;</span>
  <span class="nav-dots">&lsaquo; &rsaquo;</span>
  <p style="top:26px">It is a long established fact that a reader will be distracted by the readable content of a page when looking at its layout.<br>The point of using Lorem Ipsum is that it has a more-or-less normal distribution of letters...</p>
  <p style="top:78px;line-height:13px">Mira Hanley<br>Pathologists Researcher</p>
</div>
<section class="abs about">
  <h2 class="section">About</h2>
  <div class="brand-small">Lantern Pathway</div>
  <p>Lantern Pathway is part of the Brightwell Learning Group of Companies, who are providing speech language therapy, occupational therapy and educational therapy services to both the Singapore and the international school community.</p>
  <p>Lantern Pathway aims to work in an integrated manner, respecting the work of the respective professionals involved and collaborating effectively.</p>
  <span class="btn-grey">Click here for Read more</span>
</section>
<section class="abs support">
  <h2 class="section">Shadow Support</h2>
  <div class="item">
    <div class="icon"><svg width="24" height="24" viewBox="0 0 24 24" stroke="#fff" stroke-width="2.4" stroke-linecap="round"><path d="M5 19L17 7M5 5l14 14M15 5l4 4"/></svg></div>
    <div><h4>What is shadow support?</h4><p>A shadow support is para-professional who can help a struggling student to integrate and learn in their school environment...</p><div class="more">[ Read More + ]</div></div>
  </div>
  <div class="item">
    <div class="icon"><svg width="22" height="26" viewBox="0 0 22 26" fill="none" stroke="#fff" stroke-width="1.6"><rect x="2" y="3" width="18" height="22" rx="2"/><rect x="7" y="1" width="8" height="4" rx="1"/><path d="M5 10h2M10 10h7M5 15h2M10 15h7M5 20h2M10 20h7"/></svg></div>
    <div><h4>What are its Advantages?</h4><p>A fully trained shadow support is an asset to the student who otherwise would have trouble fitting in and adapting to the mainstream school environment...</p><div class="more">[ Read More + ]</div></div>
  </div>
  <div class="item">
    <div class="icon"><svg width="24" height="24" viewBox="0 0 24 24" fill="none" stroke="#fff" stroke-width="1.8"><circle cx="12" cy="12" r="10"/><path d="M8 15q4 3 8 0M9 10h.1M15 10h.1"/></svg></div>
    <div><h4>How do I know if my child needs shadowing</h4><p>A consultation with our Speech Language Pathologist, along with an assessment by an Educational Psychologist would provide us with an indication...</p><div class="more">[ Read More + ]</div></div>
  </div>
</section>
<div class="abs register">
  <svg class="abs" width="618" height="57" style="left:0;top:0"><path d="M0.5 0.5H597L617 28.5L597 56.5H0.5Z" fill="var(--light)" stroke="#d6d6d6"/><path d="M472 14H582L598 29L582 44H472Z" fill="#5f6670"/></svg>
  <div class="txt"><h3>Register as a Shadow</h3><p>If unsure whether your child will benefit from Shadow Support, please speak to your child's Speech Language Pathologist.</p></div>
  <div class="req">Request Now</div>
</div>
<div class="abs services-head"><h2 class="section">Our Services</h2><p>We provide a full fledged, seamless service that serves to:</p></div>
<div class="abs svc" style="left:124px"><div class="ph" role="img" aria-label="Photo of clinicians examining samples" style="background:linear-gradient(110deg,#9fb7cf,#e9edf1 55%,#c8a58a)"></div><h4>Train shadows</h4><p>Train shadows with a strong focus on equipping them with dynamic, clinical skills.</p></div>
<div class="abs svc" style="left:338px"><div class="ph" role="img" aria-label="Photo of a smiling family" style="background:linear-gradient(110deg,#7fa7c2,#e6d3c0 50%,#d8b692)"></div><h4>Provide families</h4><p>Provide families with well-trained Shadows who are mentored by Speech Language Pathologists and Professional Therapists to carry out shadow support.</p></div>
<div class="abs svc" style="left:551px"><div class="ph" role="img" aria-label="Photo of a client in a consultation session" style="background:linear-gradient(110deg,#5a3a2c,#2f7fc4 50%,#c9a98e)"></div><h4>Work with educational</h4><p>Work with educational professionals (Educational Psychologists) to provide an effective solution to the learning needs of a student.</p></div>
<footer class="abs footer">
  <div class="links">Home &nbsp;&nbsp;| &nbsp;&nbsp;About Us &nbsp;&nbsp;| &nbsp;&nbsp;Services &nbsp;&nbsp;| &nbsp;&nbsp;Shadow Support &nbsp;&nbsp;| &nbsp;&nbsp;For Referrers &nbsp;&nbsp;| &nbsp;&nbsp;Contact us</div>
  <div class="copy">Copyright © 2014. Lantern Pathway. All Rights Reserved</div>
  <div class="follow">Follow Us : <span class="c" style="background:#3b5ba0"></span><span class="c" style="background:#3aa6dc"></span><span class="c" style="background:#1c7aa8"></span><span class="c" style="background:#444"></span><span class="c" style="background:#d42b2b"></span></div>
</footer>
</body>
</html>
```